Box design for superfood powders

Hey,
I am creating a new brand of superfoods mixes in and I am looking for a designer to create the design for the box.
I have for 4 products on the roadmap, but I need the design just for the first one:
- For skin nails and hair benefits: Collagen + CoQ10 and Vitamin C powders (eg: Blueberries, Camu Camu, Acai)
- For energy and immune system (eg: mushrooms powder)
- Green Mix (eg: Spirulina + Wheatgrass + Chlorella)
- Protein mix (eg: hemp + rice powders)
I will use Kraft paper for the box so I am able to print max 2 colors on them (black and another color distinctive for each specific powder mix).
I need the design just for the first one with collagen, because all the products will have the same format. I will just change the name, ingredients and the color
More details in the archive attached.

Updates
Low design quality
Target Market(s)
woman between 30-50
Requirements
Should not have
- Ilustrations with fruits or flowers
Just shapes and colors

```html
<!DOCTYPE html>
<html lang="en">
<head>
<meta charset="utf-8">
<title>Lumora Radiant Collagen – box panels</title>
<link href="https://fonts.googleapis.com/css2?family=Poppins:wght@400;500;600;700;800&display=swap" rel="stylesheet">
<style>
  :root {
    --kraft: #c4996b;
    --violet: #574a93;
    --ink: #0d0b0a;
    --white: #ffffff;
  }
  * { margin: 0; padding: 0; box-sizing: border-box; }
  html, body { width: 1200px; height: 1000px; overflow: hidden; background: var(--white); }
  body { position: relative; font-family: "Poppins", sans-serif; color: var(--ink); }

  .panel { position: absolute; background: var(--kraft); overflow: hidden; }
  .panel--back { left: 112px; top: 443px; width: 278px; height: 379px; }
  .panel--sachet { left: 410px; top: 443px; width: 279px; height: 379px; }
  .panel--front { left: 708px; top: 226px; width: 379px; height: 598px; }

  .brand-band { position: absolute; background: var(--violet); text-align: center; }
  .brand-band__frame { position: absolute; border: 1px solid var(--kraft); border-top: none; }
  .brand-name { position: absolute; left: 0; right: 0; color: var(--kraft); font-weight: 600; letter-spacing: -0.5px; line-height: 1; white-space: nowrap; }
  .brand-tagline { position: absolute; left: 0; right: 0; color: var(--kraft); font-weight: 500; line-height: 1; white-space: nowrap; }

  .title { position: absolute; left: 0; right: 0; text-align: center; font-weight: 800; line-height: 1; color: var(--ink); white-space: nowrap; }
  .subtitle { position: absolute; left: 0; right: 0; text-align: center; font-weight: 500; line-height: 1; white-space: nowrap; }

  .flavour { position: absolute; border-top: 1px solid var(--violet); border-bottom: 1px solid var(--violet); text-align: center; font-weight: 400; display: flex; align-items: center; justify-content: center; white-space: nowrap; }

  .weight-box { position: absolute; background: var(--violet); color: var(--kraft); text-align: center; display: flex; flex-direction: column; justify-content: center; line-height: 1.1; }

  /* sachet */
  .panel--sachet .brand-band { left: 77px; top: 0; width: 123px; height: 162px; }
  .panel--sachet .brand-band__frame { left: 7px; top: 0; width: 110px; height: 155px; }
  .panel--sachet .brand-name { top: 90px; font-size: 31px; }
  .panel--sachet .brand-tagline { top: 128px; font-size: 7.5px; }
  .panel--sachet .title--l1 { top: 180px; font-size: 25px; }
  .panel--sachet .title--l2 { top: 204px; font-size: 25px; }
  .panel--sachet .title--l3 { top: 227px; font-size: 19px; }
  .panel--sachet .subtitle { top: 249px; font-size: 10.5px; }
  .panel--sachet .flavour { left: 64px; top: 285px; width: 160px; height: 17px; font-size: 9.5px; }
  .panel--sachet .weight-box { left: 76px; top: 336px; width: 125px; height: 43px; font-size: 15px; }

  /* front */
  .panel--front .brand-band { left: 86px; top: 0; width: 197px; height: 221px; }
  .panel--front .brand-band__frame { left: 11px; top: 0; width: 175px; height: 210px; }
  .panel--front .brand-name { top: 102px; font-size: 52px; }
  .panel--front .brand-tagline { top: 166px; font-size: 12px; }
  .panel--front .title--l1 { top: 249px; font-size: 40px; }
  .panel--front .title--l2 { top: 284px; font-size: 40px; }
  .panel--front .title--l3 { top: 320px; font-size: 32px; }
  .panel--front .subtitle { top: 358px; font-size: 15.5px; }
  .panel--front .flavour { left: 59px; top: 437px; width: 261px; height: 29px; font-size: 15.5px; }
  .panel--front .weight-box { left: 86px; top: 522px; width: 197px; height: 76px; }
  .weight-box__portions { font-size: 14.5px; }
  .weight-box__net { font-size: 19px; font-weight: 500; }

  /* back */
  .nutrition { position: absolute; left: 31px; top: 37px; width: 119px; border: 1px solid var(--violet); padding: 4px 6px 3px; font-size: 6.8px; line-height: 8.1px; }
  .nutrition__head { font-weight: 600; font-size: 6.8px; border-bottom: 1px solid var(--violet); padding-bottom: 3px; margin-bottom: 3px; white-space: nowrap; }
  .nutrition__row { display: flex; justify-content: space-between; }
  .nutrition__row--sub { padding-left: 8px; }
  .about { position: absolute; left: 31px; top: 131px; font-size: 8px; line-height: 12.7px; letter-spacing: 0.35px; white-space: nowrap; }
  .ingredients { position: absolute; left: 161px; top: 30px; font-size: 7.8px; line-height: 11.4px; white-space: nowrap; }
  .usage { position: absolute; left: 161px; top: 151px; font-size: 7.8px; line-height: 11.4px; font-weight: 500; white-space: nowrap; }
  .storage { position: absolute; left: 161px; top: 208px; font-size: 7.8px; line-height: 11.4px; font-weight: 500; white-space: nowrap; }
  .usage b, .storage b { font-weight: 700; }
  .badges { position: absolute; left: 158px; top: 242px; width: 110px; height: 58px; }
  .producer { position: absolute; left: 0; width: 176px; text-align: center; font-size: 7.6px; line-height: 9.6px; font-weight: 500; white-space: nowrap; }
  .producer--made { top: 286px; }
  .producer--contact { top: 313px; }
</style>
</head>
<body>

<!-- Back panel -->
<section class="panel panel--back">
  <div class="nutrition">
    <div class="nutrition__head">NUTRITIONAL VALUES/per100g</div>
    <div class="nutrition__row"><span>Energy</span><span>424.1 kcl</span></div>
    <div class="nutrition__row"><span>Fat</span><span>22 g</span></div>
    <div class="nutrition__row nutrition__row--sub"><span>Saturated</span><span>3.0 g</span></div>
    <div class="nutrition__row"><span>Carbs</span><span>29.2 g</span></div>
    <div class="nutrition__row nutrition__row--sub"><span>Sugar</span><span>16.6 g</span></div>
    <div class="nutrition__row"><span>Fibers</span><span>25.7 g</span></div>
    <div class="nutrition__row"><span>Protein</span><span>14.6 g</span></div>
    <div class="nutrition__row"><span>Salts</span><span>0.02 g</span></div>
  </div>
  <p class="about">We make it easy for busy<br>people to look and feel good<br>about their appearance. Just<br>add Radiant Collagen pow-<br>der to your favorite smoothie<br>or milk and get the extra dose<br>of collagen and skin protecting<br>antioxidants. It helps combat<br>the effects of free radicals and<br>may restore your natural<br>plumpness.</p>
  <div class="ingredients">Ingredients:<br>Type 1 Marine Collagen<br>CoQ10<br>Hyaluronic acid powder<br>Camu Camu<br>Rosehip<br>Sea buckthorn<br>Banana<br>Date<br>Acai</div>
  <p class="usage"><b>How to use it:</b> Add one<br>pack to your water,<br>smoothies, yoghurt,<br>musli, oatmeal</p>
  <p class="storage"><b>Storage:</b> Keep closed in<br>a cool dry place</p>
  <svg class="badges" viewBox="0 0 110 58" aria-hidden="true">
    <g fill="var(--violet)">
      <circle cx="11" cy="11" r="9"/><circle cx="35" cy="11" r="9"/><circle cx="59" cy="11" r="9"/><circle cx="82" cy="11" r="9"/>
      <circle cx="20" cy="43" r="9"/><circle cx="47" cy="43" r="9"/><circle cx="72" cy="43" r="9"/>
    </g>
  </svg>
  <p class="producer producer--made">Produced by:<br>Norvi SRL for Brightpath SRL</p>
  <p class="producer producer--contact">Connect:<br>Call +40 111 222 333 or visit our<br>website www.lumora.com/ro/start</p>
</section>

<!-- Sachet -->
<section class="panel panel--sachet">
  <div class="brand-band">
    <div class="brand-band__frame"></div>
    <div class="brand-name">lumora</div>
    <div class="brand-tagline">brighten your every day</div>
  </div>
  <h1 class="title title--l1">RADIANT</h1>
  <div class="title title--l2">COLLAGEN</div>
  <div class="title title--l3">+ CoQ10</div>
  <div class="subtitle">and Vitamin C powders</div>
  <div class="flavour">BLUEBERRIES, CAMU CAMU, ACAI</div>
  <div class="weight-box">10g ℮</div>
</section>

<!-- Box front -->
<section class="panel panel--front">
  <div class="brand-band">
    <div class="brand-band__frame"></div>
    <div class="brand-name">lumora</div>
    <div class="brand-tagline">brighten your every day</div>
  </div>
  <div class="title title--l1">RADIANT</div>
  <div class="title title--l2">COLLAGEN</div>
  <div class="title title--l3">+ CoQ10</div>
  <div class="subtitle">and Vitamin C powders</div>
  <div class="flavour">BLUEBERRIES, CAMU CAMU, ACAI</div>
  <div class="weight-box">
    <span class="weight-box__portions">14 PORTIONS X 10G</span>
    <span class="weight-box__net">NET WT 140G</span>
  </div>
</section>

</body>
</html>
```